依頼詳細
1.ターゲット層は30〜60代の投資家ですが、60代が多めです。

2.グローバルナビ含め、トップページ内のコンテンツは同じですが、各コンテンツの掲載箇所等にこだわりはありませんので自由にデザインして下さい。

3.コンテンツエリアは、2カラム(メイン・右ナビ)で
それぞれのサイズは下記になります。
・メイン:650px
・右ナビ:300px
(メインと右ナビの間が10px)

4.できるだけ幅広いデザインを頂きたいため、
デザインのイメージ等はこちらから指示致しません。
※ご不明点はご質問ください。

5.なおトップロゴは現行のものを利用しますのでデザインの必要ありません。
広告箇所も同じくデザインの必要はありません。
※デザインの必要が無い箇所は添付赤枠部分となります。
※広告はデザインに合わせて配置いたしますので広告箇所をご指定頂く必要はありませ

ご不明な点がありましたら、お気軽にご連絡ください。
サイトURL
http://zerinol.jp/
ページ数
3ページ
希望イメージ
シンプル 複雑
単色 カラフル
暗い 明るい
日常 高級
遊び心 厳粛
未来的 伝統的
女性的 男性的
希望する色
納品ファイル
• イラストレーター形式 (.ai)
• フォトショップ形式 (.psd)
補足説明
基本のフォントサイズも特に指定ございません。

当選者については、アイコンなどになる部分に関して、決定後、切り出しやすいように定義していただきます。

【契約上のご注意】
・採用対象となる方には当社フォーマットの契約書を締結させて頂きます。
※添付「クラウドソーシング向け業務委託契約書_提示締結用.pdf」
【10月21日追記】
提案数が1件しか集まっていないため、募集期間を1週間延長させました。

新期限:10/28

既にご提案頂いた方、当初の期限までにご提案頂く予定だった方は大変申し訳ございません。
もう暫くお待ち下さい。
たくさんのご提案をいただきありがとうございます。
お礼ご返信も間に合っておりませんが、ご返信していないご提案も
全て検討対象とさせて頂きますのでご安心ください。

今後のスケジュールに関しまして追記させて頂きます。
ご提案頂いたデザインを当社上層部に提出し社内検討をさせて頂きます。

上層部スケジュールを合わせて会議を実施・決定の流れになりますので、
日程調整等でもう暫くお時間を頂戴できればと存じます。
■ 選んだ理由

色合いや全体イメージを社内複数人による多数決により決定させていただきました。

■ 提案者全員のお礼・コメント

たくさんのご応募ありがとうございました。
本件につきましては社内調整等、
選定まで時間がかかりましたことお詫びいたします。

また本コンペは3件の当選予定をしておりまして、
今回決定の1件以外に別途2名の方に個別にプロジェクト形式でご発注させていただいております。

```html
<!DOCTYPE html>
<html lang="ja">
<head>
<meta charset="utf-8">
<title>Zerinol 株式ニュース</title>
<link href="https://fonts.googleapis.com/css2?family=Noto+Sans+JP:wght@400;500;700&display=swap" rel="stylesheet">
<style>
:root{
  --red:#c4161c;
  --red-dark:#9e1015;
  --red-soft:#fbeaea;
  --ink:#2b2b2b;
  --sub:#666;
  --line:#dcdcdc;
  --bg:#f3f3f3;
  --panel:#ffffff;
  --navy:#1d2633;
  --navy-row:#27313f;
  --up:#d0021b;
  --down:#1565c0;
  --gold:#f6c500;
}
*{box-sizing:border-box;margin:0;padding:0}
html,body{width:1200px;height:2736px;overflow:hidden}
body{background:var(--bg);font-family:"Noto Sans JP",sans-serif;color:var(--ink);font-size:13px;line-height:1.5}
.wrap{width:960px;margin:0 auto;position:relative}
a{color:inherit;text-decoration:none}

/* header */
.site-header{background:#fff;border-top:4px solid var(--red);height:112px}
.header-top{height:56px;display:flex;align-items:center;justify-content:space-between}
.brand{display:flex;align-items:center;gap:8px}
.brand-mark{width:22px;height:22px;background:var(--red)}
.brand-name{font-size:26px;font-weight:700;color:var(--red)}
.brand-tag{font-size:10px;color:var(--sub);margin-left:6px}
.header-tools{display:flex;align-items:center;gap:10px;font-size:11px;color:var(--sub)}
.search{width:260px;height:26px;border:1px solid var(--line);border-radius:3px;display:flex;align-items:center;padding:0 8px;color:#aaa}
.search-btn{width:42px;height:26px;background:var(--red);color:#fff;border-radius:3px;display:flex;align-items:center;justify-content:center;font-size:11px}
.global-nav{height:52px;border-top:1px solid var(--line);border-bottom:3px solid var(--red);display:flex}
.global-nav a{flex:1;display:flex;align-items:center;justify-content:center;gap:6px;font-size:14px;font-weight:700;border-right:1px solid var(--line)}
.global-nav a:first-child{border-left:1px solid var(--line);color:var(--red)}
.nav-ico{width:16px;height:16px}

/* ad strip */
.promo-row{display:flex;gap:10px;margin-top:10px;height:178px}
.promo-main{width:650px;display:flex;gap:8px;background:#fff;padding:4px;border:1px solid var(--line)}
.promo{flex:1;position:relative;overflow:hidden;display:flex;flex-direction:column;justify-content:flex-end;padding:10px}
.promo-photo{background:linear-gradient(160deg,#e9e4dc,#b9b1a5)}
.promo-photo span{background:#fff;font-size:20px;font-weight:700;padding:2px 8px;align-self:flex-start}
.promo-red{background:var(--red);color:#fff;justify-content:center;align-items:center;text-align:center}
.promo-red b{font-size:34px;background:#fff;color:var(--red);padding:0 10px;margin-bottom:8px}
.promo-gold{background:var(--gold);align-items:center;justify-content:center;text-align:center}
.promo-gold .day{background:var(--red);color:#fff;font-size:13px;padding:2px 8px;margin-bottom:6px}
.promo-gold .big{font-size:38px;font-weight:700;color:var(--red);line-height:1}
.promo-gold .sm{font-size:13px;font-weight:700;margin-top:8px;background:#fff;padding:2px 8px}
.index-panel{width:300px;background:var(--navy);color:#fff;padding:6px}
.index-row{height:41px;display:flex;align-items:center;border-bottom:1px solid #3a4556;padding:0 6px;gap:8px}
.flag{width:22px;height:15px;background:#8a94a3;flex-shrink:0}
.index-name{font-size:11px;color:#b9c2cf;width:66px;white-space:nowrap;flex-shrink:0}
.index-val{font-size:17px;font-weight:700;flex:1;text-align:right;white-space:nowrap}
.pct{background:var(--up);font-size:12px;font-weight:700;padding:1px 6px;border-radius:2px;width:58px;text-align:center;flex-shrink:0}
.pct.down{background:var(--down)}

/* columns */
.columns{display:flex;gap:10px;margin-top:10px}
.main-col{width:650px}
.side-col{width:300px}
.subtabs{height:28px;display:flex;gap:4px;font-size:11px;margin-bottom:10px}
.subtabs span{background:#fff;border:1px solid var(--line);padding:4px 10px}
.subtabs span.on{background:var(--red);color:#fff;border-color:var(--red)}
.panel{background:var(--panel);border:1px solid var(--line);margin-bottom:16px}
.panel-head{height:40px;display:flex;align-items:center;justify-content:space-between;border-bottom:2px solid var(--red);padding:0 12px}
.panel-title{font-size:18px;font-weight:700;color:var(--red);display:flex;align-items:center;gap:8px}
.panel-title small{font-size:11px;color:var(--sub);font-weight:400}
.more{font-size:11px;background:var(--red);color:#fff;padding:2px 10px;border-radius:2px}
.panel-body{padding:12px;display:flex;gap:14px}
.news-list{flex:1;list-style:none;min-width:0}
.news-list li{font-size:12.5px;padding:4px 0 4px 14px;border-bottom:1px dotted var(--line);position:relative;white-space:nowrap;overflow:hidden}
.news-list li::before{content:"";position:absolute;left:2px;top:11px;width:5px;height:5px;background:var(--red)}
.news-list time{color:var(--red);font-weight:500;margin-right:6px}
.chart-box{width:230px;flex-shrink:0}
.chart-cap{font-size:11px;color:var(--sub);margin-bottom:4px}
.chart{border:1px solid var(--line);background:#fff}
.chart-promo{height:70px;margin-top:10px;background:linear-gradient(120deg,#ffd6d6,#f7a6a6)}
.btn-row{display:flex;gap:8px;padding:0 12px 12px}
.btn-row a{flex:1;text-align:center;border:1px solid var(--line);background:#f7f7f7;font-size:11.5px;padding:6px 0;border-radius:3px}
.btn-row a::before{content:"▶ ";color:var(--red);font-size:9px}
.ranking-tabs{display:flex;gap:4px;margin-bottom:8px}
.ranking-tabs span{font-size:11.5px;padding:4px 10px;border:1px solid var(--line);background:#f7f7f7}
.ranking-tabs span.on{background:var(--red);color:#fff;border-color:var(--red)}
.rank-table{width:100%;border-collapse:collapse;font-size:12px}
.rank-table th{background:#f2f2f2;font-weight:500;padding:5px;border:1px solid var(--line)}
.rank-table td{padding:6px 5px;border:1px solid var(--line);text-align:right}
.rank-table td:nth-child(2){text-align:left}
.rank-table td:first-child{text-align:center;color:var(--red);font-weight:700}
.up{color:var(--up)}
.links-list{list-style:none;padding:0 12px 12px;font-size:12px;color:var(--red)}
.links-list li{padding:2px 0}
.pop-tabs{display:flex;gap:6px;padding:10px 12px 0}
.pop-tabs span{flex:1;text-align:center;font-weight:700;font-size:13px;padding:6px 0;background:#eee;border:1px solid var(--line)}
.pop-tabs span.on{background:var(--red);color:#fff;border-color:var(--red)}
.num-list{list-style:none;padding:8px 12px 12px}
.num-list li{font-size:12.5px;padding:3px 0;border-bottom:1px dotted var(--line);white-space:nowrap;overflow:hidden}
.num-list b{display:inline-block;width:20px;height:18px;line-height:18px;text-align:center;background:var(--red);color:#fff;font-size:11px;margin-right:8px;border-radius:2px}

/* side */
.side-box{background:#fff;border:1px solid var(--line);margin-bottom:16px}
.side-head{background:var(--red);color:#fff;font-weight:700;font-size:14px;padding:6px 10px}
.word-tags{padding:8px 10px;display:flex;flex-wrap:wrap;gap:6px;font-size:11.5px}
.word-tags span{color:var(--red);border:1px solid #e5b4b4;padding:1px 6px;background:var(--red-soft)}
.topic{padding:8px 10px;border-top:1px dotted var(--line)}
.topic h4{font-size:12.5px;color:var(--red);font-weight:700;margin-bottom:2px}
.topic p{font-size:11.5px;color:var(--sub);line-height:1.55}
.idx-table{width:100%;border-collapse:collapse;font-size:12px}
.idx-table td{padding:6px 10px;border-bottom:1px solid var(--line);white-space:nowrap}
.idx-table td:nth-child(2),.idx-table td:nth-child(3){text-align:right}
.idx-date{font-size:11px;color:var(--sub);padding:6px 10px}

/* bottom */
.disclaimer{background:#fff;border:1px solid var(--line);font-size:11px;color:var(--sub);padding:12px 14px;margin-top:2px;line-height:1.7}
.site-footer{background:#fff;border-top:3px solid var(--red);margin-top:14px;height:170px}
.footer-inner{width:960px;margin:0 auto;padding:18px 0;display:flex;justify-content:space-between}
.footer-links{font-size:12px;display:flex;flex-wrap:wrap;gap:6px 16px;width:620px}
.footer-copy{font-size:11px;color:var(--sub);margin-top:16px}
.footer-brand{display:flex;align-items:center;gap:8px;align-self:flex-start}
</style>
</head>
<body>

<header class="site-header">
  <div class="wrap">
    <div class="header-top">
      <div class="brand">
        <span class="brand-mark"></span>
        <span class="brand-name">Zerinol</span>
        <span class="brand-tag">zerinol.jp 株式ニュース</span>
      </div>
      <div class="header-tools">
        <span>マイページ</span><span>ログイン</span><span>ヘルプ</span>
        <div class="search">銘柄コード・銘柄名を入力</div>
        <div class="search-btn">検索</div>
      </div>
    </div>
  </div>
  <nav class="wrap global-nav">
    <a href="#"><svg class="nav-ico" viewBox="0 0 16 16"><rect x="2" y="2" width="12" height="12" fill="none" stroke="currentColor" stroke-width="2"/><path d="M5 6h6M5 9h6M5 12h4" stroke="currentColor" stroke-width="1.5"/></svg>市場ニュース</a>
    <a href="#"><svg class="nav-ico" viewBox="0 0 16 16"><path d="M2 14V8M6 14V4M10 14V9M14 14V2" stroke="#c4161c" stroke-width="2.5"/></svg>決算速報</a>
    <a href="#"><svg class="nav-ico" viewBox="0 0 16 16"><path d="M1 12l4-5 4 3 6-8" stroke="#c4161c" stroke-width="2" fill="none"/></svg>株価注目</a>
    <a href="#"><svg class="nav-ico" viewBox="0 0 16 16"><circle cx="8" cy="8" r="6" fill="none" stroke="#c4161c" stroke-width="2"/><path d="M8 4v4l3 2" stroke="#c4161c" stroke-width="1.5" fill="none"/></svg>会社業績予想</a>
    <a href="#"><svg class="nav-ico" viewBox="0 0 16 16"><path d="M8 1a5 5 0 0 0-5 5c0 4 5 9 5 9s5-5 5-9a5 5 0 0 0-5-5z" fill="#c4161c"/><circle cx="8" cy="6" r="2" fill="#fff"/></svg>投資マップ</a>
    <a href="#"><svg class="nav-ico" viewBox="0 0 16 16"><rect x="1" y="3" width="14" height="10" fill="none" stroke="#c4161c" stroke-width="2"/></svg>範囲表示</a>
  </nav>
</header>

<div class="wrap">
  <section class="promo-row">
    <div class="promo-main">
      <div class="promo promo-photo" role="img" aria-label="株価ボードを見る投資家の写真バナー"><span>東京225平均</span></div>
      <div class="promo promo-red"><b>特報</b><div>注目銘柄を毎朝お届け</div></div>
      <div class="promo promo-gold"><div class="day">本日の</div><div class="big">Sprout</div><div class="sm">スプラウト市場概況</div></div>
    </div>
    <aside class="index-panel">
      <div class="index-row"><span class="flag"></span><span class="index-name">東京225</span><span class="index-val">15,069.46</span><span class="pct">2.12%</span></div>
      <div class="index-row"><span class="flag"></span><span class="index-name">ドル円</span><span class="index-val">107.32</span><span class="pct">0.21%</span></div>
      <div class="index-row"><span class="flag"></span><span class="index-name">中国本土</span><span class="index-val">2,199.18</span><span class="pct">2.12%</span></div>
      <div class="index-row"><span class="flag"></span><span class="index-name">スプラウト</span><span class="index-val">868.22</span><span class="pct">2.12%</span></div>
    </aside>
  </section>

  <div class="columns">
    <main class="main-col">
      <div class="subtabs"><span class="on">人気テーマ</span><span>米国30種</span><span>東京225</span><span>為替</span><span>先物</span><span>米国株</span><span>新興株</span></div>

      <section class="panel">
        <div class="panel-head"><h2 class="panel-title">TOP NEWS</h2><a class="more" href="#">最新ニュース一覧 ▶</a></div>
        <div class="panel-body">
          <ul class="news-list">
            <li><time>15:30</time>東京225平均は大幅反発、輸出関連株に買い戻し</li>
            <li><time>15:12</time>新興市場は続伸、バイオ関連の一角に物色集中</li>
            <li><time>14:58</time>円相場は107円台前半、米指標を控え様子見</li>
            <li><time>14:40</time>大手銀行株が上昇、長期金利の上昇を好感</li>
            <li><time>14:21</time>決算発表を控えた電子部品株に先回り買い</li>
            <li><time>13:55</time>後場寄り、先物主導で上げ幅を一段と拡大</li>
            <li><time>13:30</time>中国株は続伸、景気対策への期待が支え</li>
            <li><time>12:48</time>前引け、総合株価指数は8日ぶりに反発</li>
            <li><time>12:10</time>通信株が軟調、値下げ競争への警戒感が重荷</li>
            <li><time>11:35</time>不動産株が堅調、都心オフィス空室率が改善</li>
            <li><time>11:02</time>中小型株の一角に好業績銘柄を見直す動き</li>
            <li><time>10:40</time>寄り付き、東京225平均は300円超の上昇</li>
            <li><time>10:05</time>米国株市場は主要3指数そろって上昇</li>
            <li><time>09:30</time>今日の注目材料、海外投資家の売買動向</li>
          </ul>
          <div class="chart-box">
            <div class="chart-cap">東京225平均 日中足</div>
            <svg class="chart" width="230" height="170" viewBox="0 0 230 170">
              <g stroke="#eee"><line x1="0" y1="34" x2="230" y2="34"/><line x1="0" y1="68" x2="230" y2="68"/><line x1="0" y1="102" x2="230" y2="102"/><line x1="0" y1="136" x2="230" y2="136"/><line x1="46" y1="0" x2="46" y2="170"/><line x1="92" y1="0" x2="92" y2="170"/><line x1="138" y1="0" x2="138" y2="170"/><line x1="184" y1="0" x2="184" y2="170"/></g>
              <polyline points="6,30 20,36 32,34 46,50 58,46 72,62 86,58 100,80 114,78 128,96 142,104 156,100 170,118 184,130 198,126 212,142 224,150" fill="none" stroke="#c4161c" stroke-width="2"/>
              <g font-size="9" fill="#999" font-family="Noto Sans JP, sans-serif"><text x="196" y="30">15,200</text><text x="196" y="98">15,000</text></g>
            </svg>
            <div class="chart-promo" role="img" aria-label="市況チャート特集の告知バナー"></div>
          </div>
        </div>
        <div class="btn-row"><a href="#">市場概況ニュース一覧</a><a href="#">注目銘柄ニュース一覧</a><a href="#">海外市場ニュース一覧</a></div>
      </section>

      <section class="panel">
        <div class="panel-head"><h2 class="panel-title">決算速報 <small>10月21日 15:20 更新</small></h2><a class="more" href="#">決算速報一覧 ▶</a></div>
        <div class="panel-body">
          <ul class="news-list">
            <li><time>10/20 17:30</time>北洋精機、今期経常を一転増益に上方修正</li>
            <li><time>10/20 17:10</time>三河化成、上期経常は2割増で着地</li>
            <li><time>10/20 16:45</time>南海フーズ、今期配当を5円増額へ</li>
            <li><time>10/20 16:20</time>東陽システム、7-9月期は最高益を更新</li>
            <li><time>10/20 15:55</time>青葉電工、通期予想を据え置き</li>
            <li><time>10/20 15:30</time>大和精密、上期経常を下方修正</li>
            <li><time>10/20 15:10</time>北辰商事、自社株買いを発表</li>
            <li><time>10/20 15:00</time>丸星工業、今期純利益は3割減の見通し</li>
          </ul>
          <div class="chart-box">
            <div class="chart-cap">総合株価指数 日足</div>
            <svg class="chart" width="230" height="170" viewBox="0 0 230 170">
              <g stroke="#eee"><line x1="0" y1="42" x2="230" y2="42"/><line x1="0" y1="85" x2="230" y2="85"/><line x1="0" y1="128" x2="230" y2="128"/><line x1="57" y1="0" x2="57" y2="170"/><line x1="115" y1="0" x2="115" y2="170"/><line x1="172" y1="0" x2="172" y2="170"/></g>
              <polyline points="6,26 22,30 38,28 54,44 70,40 86,60 102,70 118,66 134,88 150,96 166,108 182,104 198,124 214,136 224,140" fill="none" stroke="#c4161c" stroke-width="2"/>
            </svg>
          </div>
        </div>
        <div class="btn-row"><a href="#">本日の決算発表予定</a><a href="#">業績修正一覧</a><a href="#">決算カレンダー</a></div>
      </section>

      <section class="panel">
        <div class="panel-head"><h2 class="panel-title">ランキング・注目銘柄 <small>10月21日 15:00</small></h2><a class="more" href="#">ランキング一覧 ▶</a></div>
        <div class="panel-body" style="flex-direction:column;gap:8px">
          <div class="ranking-tabs"><span class="on">上昇率</span><span>下落率</span><span>出来高</span><span>売買代金</span><span>年初来高値</span></div>
          <div style="display:flex;gap:14px">
            <table class="rank-table" style="flex:1">
              <tr><th>順位</th><th>銘柄</th><th>株価</th><th>前日比</th></tr>
              <tr><td>1</td><td>北洋精機</td><td>1,284</td><td class="up">+22.4%</td></tr>
              <tr><td>2</td><td>東陽システム</td><td>652</td><td class="up">+18.1%</td></tr>
              <tr><td>3</td><td>三河化成</td><td>2,310</td><td class="up">+15.7%</td></tr>
              <tr><td>4</td><td>青葉電工</td><td>418</td><td class="up">+13.2%</td></tr>
              <tr><td>5</td><td>南海フーズ</td><td>975</td><td class="up">+11.9%</td></tr>
              <tr><td>6</td><td>丸星工業</td><td>1,530</td><td class="up">+10.6%</td></tr>
              <tr><td>7</td><td>北辰商事</td><td>287</td><td class="up">+9.8%</td></tr>
              <tr><td>8</td><td>大和精密</td><td>3,040</td><td class="up">+9.1%</td></tr>
            </table>
            <div class="chart-box">
              <div class="chart-cap">上昇率1位 日中足</div>
              <svg class="chart" width="230" height="200" viewBox="0 0 230 200">
                <g stroke="#eee"><line x1="0" y1="50" x2="230" y2="50"/><line x1="0" y1="100" x2="230" y2="100"/><line x1="0" y1="150" x2="230" y2="150"/><line x1="77" y1="0" x2="77" y2="200"/><line x1="153" y1="0" x2="153" y2="200"/></g>
                <polyline points="6,40 20,48 34,44 48,66 62,62 76,86 90,84 104,108 118,120 132,114 146,140 160,150 174,146 188,166 202,172 224,180" fill="none" stroke="#c4161c" stroke-width="2"/>
              </svg>
            </div>
          </div>
        </div>
        <ul class="links-list"><li>▶ 値上がり率ランキング</li><li>▶ ストップ高銘柄一覧</li><li>▶ 年初来高値更新銘柄</li></ul>
      </section>

      <section class="panel">
        <div class="pop-tabs"><span class="on">人気ニュース</span><span>人気テーマ</span><span>人気ニュース(週間)</span></div>
        <ol class="num-list">
          <li><b>1</b>今週の注目株、円安進行で自動車株に再評価の動き</li>
          <li><b>2</b>東京225平均、1万5000円台回復で次の節目を探る</li>
          <li><b>3</b>高配当株特集、利回り4%超の銘柄を一挙紹介</li>
          <li><b>4</b>新興市場の人気テーマ、再生医療関連が首位に</li>
          <li><b>5</b>決算発表シーズン到来、上方修正期待の10銘柄</li>
          <li><b>6</b>株主優待の新設相次ぐ、個人投資家の関心集まる</li>
          <li><b>7</b>米金利動向と日本株、今後の見通しを解説</li>
          <li><b>8</b>海外投資家の売買動向、3週連続で買い越し</li>
          <li><b>9</b>中国景気指標を受け、素材株に買い戻し</li>
          <li><b>10</b>来週の相場展望、重要指標の発表が相次ぐ</li>
        </ol>
      </section>

      <section class="panel">
        <div class="panel-head"><h2 class="panel-title">開示情報(決算・業績修正を除く) <small>10月21日 15:00</small></h2><a class="more" href="#">一覧 ▶</a></div>
        <div class="panel-body">
          <ul class="news-list">
            <li><time>14/10/21 17:00</time>北洋精機、新工場建設に関するお知らせ</li>
            <li><time>14/10/21 16:45</time>三河化成、自己株式の取得状況について</li>
            <li><time>14/10/21 16:30</time>南海フーズ、子会社設立に関するお知らせ</li>
            <li><time>14/10/21 16:10</time>東陽システム、業務提携契約の締結について</li>
            <li><time>14/10/21 15:50</time>青葉電工、役員人事の内定に関するお知らせ</li>
            <li><time>14/10/21 15:30</time>大和精密、株式分割および定款変更について</li>
            <li><time>14/10/21 15:15</time>北辰商事、株主優待制度の新設について</li>
            <li><time>14/10/21 15:00</time>丸星工業、固定資産の譲渡に関するお知らせ</li>
            <li><time>14/10/21 14:40</time>東邦物産、新株予約権の行使状況について</li>
            <li><time>14/10/21 14:20</time>西海電機、特別損失の計上に関するお知らせ</li>
            <li><time>14/10/21 14:00</time>中央建設、受注高の月次報告について</li>
            <li><time>14/10/21 13:40</time>光和製薬、臨床試験の進捗に関するお知らせ</li>
          </ul>
        </div>
        <div class="btn-row"><a href="#">開示情報一覧を見る</a></div>
      </section>
    </main>

    <aside class="side-col">
      <section class="side-box">
        <h3 class="side-head">本日の注目ワード</h3>
        <div class="word-tags"><span>円安</span><span>再生医療</span><span>高配当</span><span>自社株買い</span><span>株主優待</span><span>上方修正</span><span>IoT</span><span>インバウンド</span></div>
        <div class="topic"><h4>円安進行で輸出株が全面高</h4><p>ドル円が107円台に乗せ、自動車や電機など輸出関連に買いが集まった。</p></div>
        <div class="topic"><h4>再生医療関連が人気化</h4><p>新興市場でバイオ株への物色が続き、出来高も大きく膨らんでいる。</p></div>
        <div class="topic"><h4>高配当株に個人の買い</h4><p>利回りの高い大型株に押し目買いが入り、下値の堅さが目立った。</p></div>
        <div class="topic"><h4>自社株買いの発表相次ぐ</h4><p>株主還元強化の流れが続き、発表銘柄は翌日に大きく上昇した。</p></div>
        <div class="topic"><h4>株主優待の新設に注目</h4><p>優待新設を発表した中小型株に、長期保有狙いの買いが入った。</p></div>
        <div class="topic"><h4>上方修正期待の銘柄群</h4><p>決算発表を前に、業績好調な企業への先回り買いが観測された。</p></div>
        <div class="topic"><h4>IoT関連が再び上昇</h4><p>通信機器や半導体の一角に、テーマ性を評価した資金が流入した。</p></div>
        <div class="topic"><h4>訪日客関連が堅調推移</h4><p>百貨店や旅行関連が買われ、消費関連株全体を下支えした。</p></div>
        <div class="topic"><h4>不動産株に見直し買い</h4><p>都心の空室率改善を受け、大手不動産株が揃って値を上げた。</p></div>
        <div class="topic"><h4>銀行株が金利上昇で反発</h4><p>長期金利の上昇を背景に、メガバンク株が相場をけん引した。</p></div>
      </section>

      <section class="side-box">
        <h3 class="side-head">指数一覧</h3>
        <div class="idx-date">2014年10月21日 15:00 現在</div>
        <table class="idx-table">
          <tr><td>東京225平均</td><td>15,069.46</td><td class="up">+313.13</td></tr>
          <tr><td>総合株価指数</td><td>1,220.44</td><td class="up">+24.69</td></tr>
          <tr><td>新興総合</td><td>2,186.62</td><td class="up">+19.08</td></tr>
          <tr><td>スプラウト指数</td><td>868.22</td><td class="up">+18.01</td></tr>
          <tr><td>ドル円</td><td>107.32</td><td class="up">+0.22</td></tr>
          <tr><td>ユーロ円</td><td>136.64</td><td class="up">+0.57</td></tr>
        </table>
      </section>
    </aside>
  </div>

  <p class="disclaimer">当サイトで提供する情報は投資判断の参考として情報提供を目的としたものであり、投資の勧誘を目的としたものではありません。掲載情報の正確性には万全を期しておりますが、その内容を保証するものではありません。投資に関する最終決定はご自身の判断でお願いいたします。</p>
</div>

<footer class="site-footer">
  <div class="footer-inner">
    <div>
      <div class="footer-links"><span>利用上のご注意</span><span>利用規約</span><span>個人情報保護方針</span><span>会社概要</span><span>広告掲載について</span><span>お問い合わせ</span><span>サイトマップ</span><span>ヘルプ</span></div>
      <p class="footer-copy">© 2014 Zerinol Inc. All Rights Reserved. zerinol.jp</p>
    </div>
    <div class="footer-brand"><span class="brand-mark"></span><span class="brand-name">Zerinol</span></div>
  </div>
</footer>

</body>
</html>
```